corvana ridge bathrooms

We are in the business of renovating peoples bathrooms and tiling service

we provide a total solution from design to reconstruction of your bathroom

we would like a 5 page website

please design the home page first so we choose design then complete the other 4 pages i have uploaded the logo

Industry/Entity Type

Business

```html
<!DOCTYPE html>
<html lang="en">
<head>
<meta charset="utf-8">
<title>Corvana Ridge Homes</title>
<link rel="stylesheet" href="https://fonts.googleapis.com/css2?family=Source+Sans+3:wght@400;600;700&family=Hind:wght@400;500;600&family=Questrial&display=swap">
<style>
  :root {
    --page-top: #f7f6f5;
    --page-bottom: #ebe7e4;
    --nav-bg: #4b4b4b;
    --nav-active: #a31f24;
    --nav-text: #ffffff;
    --brand-gold: #a1831b;
    --heading: #636363;
    --body-text: #5e5e5e;
    --muted: #777777;
    --button-grey: #a8a5a2;
    --footer-bg: #2b2e30;
    --footer-text: #b4b8bb;
    --overlay: rgba(58, 58, 58, 0.82);
    --hero-band: #dedddc;
  }
  * { box-sizing: border-box; margin: 0; padding: 0; }
  html, body { width: 1172px; height: 1200px; overflow: hidden; }
  body {
    position: relative;
    font-family: "Hind", "Source Sans 3", sans-serif;
    background: linear-gradient(180deg, var(--page-top) 0%, var(--page-bottom) 100%);
    color: var(--body-text);
  }
  a { color: inherit; text-decoration: none; }

  /* Header */
  .site-header { position: absolute; left: 0; top: 0; width: 1172px; height: 187px; }
  .brand {
    position: absolute; left: 36px; top: 70px;
    display: flex; align-items: center; gap: 12px;
    font-family: "Source Sans 3", sans-serif; font-weight: 700;
    font-size: 26px; letter-spacing: 0.5px; color: var(--brand-gold);
    text-transform: uppercase;
  }
  .brand-mark { width: 22px; height: 22px; background: var(--brand-gold); }
  .account-links {
    position: absolute; right: 36px; top: 36px;
    font-size: 13px; color: var(--muted);
  }
  .search-box {
    position: absolute; left: 902px; top: 139px; width: 235px; height: 25px;
    border: 1px solid #b9b9b9; background: #ffffff;
    font-size: 12.5px; color: #9a9a9a; padding: 4px 0 0 10px;
  }
  .search-box svg { position: absolute; right: 8px; top: 5px; }

  /* Navigation */
  .main-nav {
    position: absolute; left: 0; top: 187px; width: 1172px; height: 37px;
    background: var(--nav-bg);
  }
  .main-nav a {
    position: absolute; top: 0; height: 37px; line-height: 39px;
    font-size: 16.5px; color: var(--nav-text); letter-spacing: 0.3px;
  }
  .main-nav a.is-active { background: var(--nav-active); text-align: center; }

  /* Hero */
  .hero { position: absolute; left: 34px; top: 224px; width: 1103px; height: 391px; background: var(--hero-band); }
  .hero-photo {
    position: absolute; left: 0; top: 46px; width: 1103px; height: 345px;
    background: linear-gradient(90deg, #5a5654 0%, #b04a4a 22%, #c9c4c1 45%, #d4d0cd 58%, #8ea9c3 72%, #7f9fbf 100%);
  }
  .hero-caption {
    position: absolute; left: 626px; top: 145px; width: 477px; height: 220px;
    background: var(--overlay); padding: 30px 20px 0 27px; color: #ffffff;
  }
  .hero-caption h1 {
    font-family: "Questrial", sans-serif; font-weight: 400;
    font-size: 26px; white-space: nowrap; margin-left: -3px; line-height: 1.1;
  }
  .hero-caption p { width: 410px; font-weight: 600; font-size: 15px; line-height: 25px; margin-top: 8px; }
  .hero-button {
    display: block; margin: 14px 0 0 2px; width: 150px; height: 36px;
    background: #ffffff; color: #555; font-weight: 600; font-size: 14.5px;
    text-align: center; line-height: 38px;
  }

  /* Content */
  .feature { position: absolute; }
  .feature h2 {
    font-family: "Source Sans 3", sans-serif; font-weight: 600;
    color: var(--heading); letter-spacing: -0.2px; line-height: 1;
  }
  .feature p { font-size: 14.5px; line-height: 25px; letter-spacing: 0.3px; color: var(--body-text); }
  .feature--main { left: 38px; width: 632px; }
  .feature--main h2 { font-size: 35px; }
  .feature--main p { width: 626px; margin: 20px 0 0 2px; }
  .feature--side { left: 734px; width: 360px; }
  .feature--side h2 { font-size: 27px; }
  .feature--side p { width: 325px; margin: 17px 0 0 4px; }
  .more-button {
    position: absolute; width: 113px; height: 30px; background: var(--button-grey);
    color: #ffffff; font-weight: 600; font-size: 14px; text-align: center; line-height: 32px;
  }

  /* Footer */
  .site-footer {
    position: absolute; left: 0; top: 1137px; width: 1172px; height: 63px;
    background: var(--footer-bg); color: var(--footer-text); font-size: 13px;
  }
  .footer-list { position: absolute; top: 11px; display: flex; }
  .footer-list span { padding: 0 10px; border-left: 1px solid var(--footer-text); line-height: 15px; }
  .footer-list span:first-child { border-left: none; padding-left: 0; }
  .footer-list--nav span { padding: 0 16px; }
  .footer-list--nav span:last-child { padding-right: 0; }
</style>
</head>
<body>
  <header class="site-header">
    <div class="brand"><span class="brand-mark"></span>Corvana Ridge Homes</div>
    <div class="account-links">Login or Register</div>
    <div class="search-box">Search
      <svg width="14" height="14" viewBox="0 0 14 14" fill="none" stroke="#8a8a8a" stroke-width="1.3">
        <circle cx="8.5" cy="5.5" r="4"/><line x1="5.6" y1="8.4" x2="1.5" y2="12.5"/>
      </svg>
    </div>
  </header>

  <nav class="main-nav">
    <a style="left:46px">Home</a>
    <a style="left:147px">Bathrooms</a>
    <a style="left:279px">Tiles</a>
    <a style="left:362px">Reconstructions</a>
    <a class="is-active" style="left:514px;width:158px">Total Solutions</a>
    <a style="left:705px">About</a>
    <a style="left:802px">Contact</a>
  </nav>

  <section class="hero">
    <div class="hero-photo" role="img" aria-label="Modern bathroom with a red freestanding bathtub and red rug beside a window overlooking the sea"></div>
    <div class="hero-caption">
      <h1>Welcome to Corvana Ridge Homes</h1>
      <p>Viderer alienum apeirian pri no. An sed labitur expetendis moderatius. Te vis animal alterum torquatos, eum suas simul nonumes id. Nonumes moderatius sit ad, quaeque</p>
      <a class="hero-button">Read more</a>
    </div>
  </section>

  <article class="feature feature--main" style="top:659px">
    <h2>Main Title Goes Here</h2>
    <p>Viderer alienum apeirian pri no. An sed labitur expetendis moderatius. Te vis animal alterum torquatos, eum suas simul nonumes id. Nonumes moderatius sit ad, quaeque similique mel ea, an platonem liberavisse mediocritatem has. Ex sed volutpat voluptatum. Libris percipit per ei, mandamus voluptatibus eos ut.</p>
  </article>
  <a class="more-button" style="left:40px;top:833px">Read more</a>

  <article class="feature feature--main" style="top:898px">
    <h2>Another Title Goes Here</h2>
    <p>Viderer alienum apeirian pri no. An sed labitur expetendis moderatius. Te vis animal alterum torquatos, eum suas simul nonumes id. Nonumes moderatius sit ad, quaeque similique mel ea, an platonem liberavisse mediocritatem has. Ex sed volutpat voluptatum. Libris percipit per ei, mandamus voluptatibus eos ut.</p>
  </article>
  <a class="more-button" style="left:40px;top:1073px">Read more</a>

  <article class="feature feature--side" style="top:669px">
    <h2>Small Title One Goes Here</h2>
    <p>Viderer alienum apeirian pri no. An sed labitur expetendis moderatius. Te vis animal alterum torquatos, eum suas simul nonumes id. Nonumes moderatius sit ad, quaeque similique</p>
  </article>
  <a class="more-button" style="left:739px;top:833px">Read more</a>

  <article class="feature feature--side" style="top:903px">
    <h2>Small Title Two Goes Here</h2>
    <p>Viderer alienum apeirian pri no. An sed labitur expetendis moderatius. Te vis animal alterum torquatos, eum suas simul nonumes id. Nonumes moderatius sit ad, quaeque similique</p>
  </article>
  <a class="more-button" style="left:739px;top:1073px">Read more</a>

  <footer class="site-footer">
    <div class="footer-list" style="left:40px">
      <span>Copyright 2013</span><span>Corvana Ridge Homes</span><span>All Rights Reserved</span>
    </div>
    <div class="footer-list footer-list--nav" style="right:36px">
      <span>Home</span><span>Bathrooms</span><span>Tiles</span><span>About</span><span>Contact</span>
    </div>
  </footer>
</body>
</html>
```